Illustrations for a Project Management Concept

we need illustrations for 5 project management principles that make up a holistic approach to project management, without all the BS. if we extract all the methodology, system, tool and mumbo-jumbo out of project management, we end up with some essential principles that are simple to understand and use. It's likely that people who use them will not be traditional Project Management types.

I've mocked up something that looks very corporate based on a template, but this has the wrong tone; the wrong feeling. I'd like something "funky" and colorful that conveys "Action" within "Simplicity".

the PPT file with the dark-blue background is the "corporate" consulting type mockup. the PPT with the white background shows an idea I had for breaking out each of the 5 principles (only one shown) to make it larger, with some text in a callout.

In the final deliverable, I need to be able to both show all 5 on one diagram, as well as slicing the image to display each principle separately. i do not have editing capabilities for vector image formats, only image formats

Reason: there are a number of designers who have only just accepted the invitation. I want to give everyone a chance to submit.

```html
<!DOCTYPE html>
<html lang="en">
<head>
<meta charset="UTF-8">
<title>5 Project Action Principles</title>
<link rel="stylesheet" href="https://fonts.googleapis.com/css2?family=Nunito:wght@800&family=Roboto:ital,wght@1,300&display=swap">
<style>
  :root {
    --canvas-bg: #4a4a4a;
    --ring-shadow: #2c2c2c;
    --ring-inner: #474747;
    --orange: #e8905f;
    --orange-dark: #c66f3f;
    --blue: #1e8ae6;
    --blue-dark: #0e62b5;
    --green: #22b23c;
    --green-dark: #138a28;
    --purple: #9a2fc2;
    --purple-dark: #6e1a92;
    --sphere-light: #9fd2ff;
    --sphere-mid: #3d95e6;
    --sphere-dark: #14539b;
    --chevron: #d4d4d4;
    --chevron-shade: #a9a9a9;
    --label: #ffffff;
    --panel-bg: #000000;
    --panel-text: #d8d8d8;
  }
  * { box-sizing: border-box; }
  html, body {
    margin: 0;
    padding: 0;
    overflow: hidden;
    background: var(--canvas-bg);
  }
  .canvas {
    position: relative;
    width: 1200px;
    height: 675px;
    overflow: hidden;
    background: var(--canvas-bg);
  }
  .wheel {
    position: absolute;
    left: 0;
    top: 0;
    width: 1200px;
    height: 675px;
  }
  .segment-label {
    font-family: "Nunito", "Verdana", sans-serif;
    font-weight: 800;
    font-size: 25px;
    letter-spacing: 0.5px;
    fill: var(--label);
  }
  .hub-label {
    font-family: "Nunito", "Verdana", sans-serif;
    font-weight: 800;
    font-size: 22px;
    fill: var(--label);
  }
  .principles-panel {
    position: absolute;
    left: 772px;
    top: 82px;
    width: 363px;
    height: 465px;
    background: var(--panel-bg);
    border-radius: 22px;
    box-shadow: 0 6px 14px rgba(0,0,0,0.45);
    padding: 36px 28px 0 28px;
    font-family: "Roboto", "Helvetica", sans-serif;
    font-style: italic;
    font-weight: 300;
    color: var(--panel-text);
    letter-spacing: 1.6px;
  }
  .principles-title {
    margin: 0 0 38px 0;
    font-size: 15px;
    font-weight: 300;
    letter-spacing: 2.2px;
  }
  .principles-list {
    list-style: none;
    margin: 0;
    padding: 0;
    font-size: 16px;
    line-height: 31.3px;
  }
</style>
</head>
<body>
<main class="canvas">
  <svg class="wheel" viewBox="0 0 1200 675" xmlns="http://www.w3.org/2000/svg" aria-label="Five principles wheel">
    <defs>
      <radialGradient id="sphere-fill" cx="38%" cy="32%" r="70%">
        <stop offset="0" stop-color="var(--sphere-light)"/>
        <stop offset="0.45" stop-color="var(--sphere-mid)"/>
        <stop offset="1" stop-color="var(--sphere-dark)"/>
      </radialGradient>
      <radialGradient id="inner-shadow" cx="50%" cy="50%" r="50%">
        <stop offset="0.85" stop-color="var(--ring-inner)"/>
        <stop offset="1" stop-color="var(--ring-shadow)"/>
      </radialGradient>
      <linearGradient id="orange-fill" x1="0" y1="0" x2="0" y2="1">
        <stop offset="0" stop-color="var(--orange)"/>
        <stop offset="1" stop-color="var(--orange-dark)"/>
      </linearGradient>
      <linearGradient id="blue-fill" x1="1" y1="0" x2="0" y2="0">
        <stop offset="0" stop-color="var(--blue)"/>
        <stop offset="1" stop-color="var(--blue-dark)"/>
      </linearGradient>
      <linearGradient id="green-fill" x1="0" y1="1" x2="0" y2="0">
        <stop offset="0" stop-color="var(--green)"/>
        <stop offset="1" stop-color="var(--green-dark)"/>
      </linearGradient>
      <linearGradient id="purple-fill" x1="0" y1="0" x2="1" y2="0">
        <stop offset="0" stop-color="var(--purple)"/>
        <stop offset="1" stop-color="var(--purple-dark)"/>
      </linearGradient>

      <path id="arc-orange" d="M160.2 248.5 A233 233 0 0 1 563.8 248.5"/>
      <path id="arc-blue" d="M478.5 163.2 A233 233 0 0 1 478.5 566.8"/>
      <path id="arc-purple" d="M245.5 566.8 A233 233 0 0 1 245.5 163.2"/>
      <path id="arc-green" d="M142 492 A254 254 0 0 0 582 492"/>
    </defs>

    <!-- wheel base -->
    <circle class="ring-base" cx="362" cy="365" r="286" fill="var(--ring-shadow)" opacity="0.35"/>
    <circle class="ring-inner" cx="362" cy="365" r="205" fill="url(#inner-shadow)"/>

    <!-- principle segments -->
    <path class="segment segment-customer" fill="url(#orange-fill)"
      d="M131 203.2 A282 282 0 0 1 584.2 191.3 L523.5 238.7 A205 205 0 0 0 194.1 247.3 Z"/>
    <path class="segment segment-models" fill="url(#blue-fill)"
      d="M590.1 199.2 A282 282 0 0 1 590.1 530.8 L527.8 485.5 A205 205 0 0 0 527.8 244.5 Z"/>
    <path class="segment segment-entropy" fill="url(#green-fill)"
      d="M584.2 538.7 A282 282 0 0 1 139.8 538.7 L200.5 491.3 A205 205 0 0 0 523.5 491.3 Z"/>
    <path class="segment segment-teaming" fill="url(#purple-fill)"
      d="M133.9 530.8 A282 282 0 0 1 133.9 199.2 L196.2 244.5 A205 205 0 0 0 196.2 485.5 Z"/>

    <!-- segment labels -->
    <text class="segment-label"><textPath href="#arc-orange" startOffset="50%" text-anchor="middle">Fulfill Customer Value</textPath></text>
    <text class="segment-label"><textPath href="#arc-blue" startOffset="50%" text-anchor="middle">Build Shared Models</textPath></text>
    <text class="segment-label"><textPath href="#arc-purple" startOffset="50%" text-anchor="middle">Eliminate Teaming Threats</textPath></text>
    <text class="segment-label"><textPath href="#arc-green" startOffset="50%" text-anchor="middle">Suppress Entropy</textPath></text>

    <!-- direction chevrons -->
    <g class="chevrons" fill="var(--chevron)" stroke="var(--chevron-shade)" stroke-width="2">
      <path class="chevron chevron-up" d="M345 198 L390 178 L435 198 L435 240 L390 222 L345 240 Z"/>
      <path class="chevron chevron-down" d="M345 448 L390 468 L435 448 L435 492 L390 510 L345 492 Z"/>
      <path class="chevron chevron-left" d="M268 295 L222 340 L268 385 L290 385 L262 340 L290 295 Z"/>
      <path class="chevron chevron-right" d="M492 295 L520 295 L556 340 L520 385 L492 385 L522 340 Z"/>
    </g>

    <!-- hub -->
    <circle class="hub-shadow" cx="376" cy="348" r="76" fill="#000" opacity="0.25"/>
    <circle class="hub" cx="372" cy="342" r="76" fill="url(#sphere-fill)"/>
    <text class="hub-label" x="372" y="334" text-anchor="middle">Achieve</text>
    <text class="hub-label" x="372" y="362" text-anchor="middle">Outcomes</text>
  </svg>

  <section class="principles-panel">
    <h1 class="principles-title">5 PROJECT ACTION PRINCIPLES</h1>
    <ol class="principles-list">
      <li>1. Achieve Outcomes,<br>Rapidly</li>
      <li>2. Fulfill Customer Value,<br>Interactively</li>
      <li>3. Build Shared Models,<br>Verifiably</li>
      <li>4. Eliminate Teaming Threats,<br>Ruthlessly</li>
      <li>5. Suppress Project Entropy,<br>Selectively</li>
    </ol>
  </section>
</main>
</body>
</html>
```